Brackenfold Latches Business Cards

Need high quality business card designed around my company logo. Ideally the cards need to be a glossy black as the logo goes well with a black background.

The company is a Locksmithing business.

Domestic clients are Residential Home Owners and Landlords. Commercial clients are local businesses, estate agents, landlords, solicitors

Services offered :
Emergency Lock Out
New Lock Fitting & Replacement
High Security Upgrades
UPVC lock repairs
Mobile Key Cutting
Free Security Reviews

Qualificatons & Certifications:
Accredited Guild & Tower KSR Level 3, QTRB
Fully Insured
PVX Checked

Contact & Business Details:

Business Name : Brackenfold Latches
Name: Rob Fenwick
Tel: 01823 574419 Office / 07841592637 Mobile
Email: contact@brackenfoldlatches.com
Website: www.brackenfoldlatches.com

(please note that the website is currently under development and not available to view)

Locksmith

Name: Rob Fenwick

Services:
Emergency Lock Out
High Security Upgrades
UPVC lock repairs
Mobile Key Cutting
Free Security Reviews

• Ideally the cards should be a glossy black as the logo stands out better on a black background.

Logo on front and the word LOCKSMITH should be incorporated into the front design of the card.

Qualifications & Certifications on the back ideally along the top / bottom of the card or split (I.e along the top “ Accredited : Guild & Tower Level 3 , QTRB”
and along the bottom , “Fully Insured & PVX Checked”

Services offered ideally listed on the back of the card, preferably split into two columns. If possible the logo could also be incorporated onto the back of the card between the two services columns (I.e the services listed either side of the logo)
• On the back of the card, have the logo in the middle with the services listed either side of the logo I.e 3 services on left of logo and three to the right.

```html
<!DOCTYPE html>
<html lang="en">
<head>
<meta charset="utf-8">
<title>Brackenfold Latches Business Cards</title>
<link rel="stylesheet" href="https://fonts.googleapis.com/css2?family=Noto+Serif:wght@400;700&family=Playfair+Display:wght@700&display=swap">
<style>
  :root {
    --backdrop: #d3d6d6;
    --card: #151516;
    --card-edge: #c99a1e;
    --gold: #d9a821;
    --gold-light: #f2cf5a;
    --silver: #c9cacc;
  }
  * { box-sizing: border-box; margin: 0; padding: 0; }
  html, body { width: 1200px; height: 1051px; overflow: hidden; }
  body {
    background: var(--backdrop);
    font-family: "Noto Serif", serif;
    position: relative;
  }
  .card {
    position: absolute;
    left: 250px;
    width: 700px;
    height: 452px;
    background: var(--card);
    border-bottom: 4px solid var(--card-edge);
    box-shadow: 0 12px 30px rgba(0,0,0,0.25);
  }
  .card-front { top: 46px; }
  .card-back { top: 553px; }

  /* Front */
  .brand-block {
    position: absolute;
    left: 40px; top: 110px;
    width: 250px;
    text-align: center;
  }
  .brand-name {
    color: var(--gold);
    font-family: "Noto Serif", serif;
    font-weight: 700;
    font-size: 30px;
    line-height: 1.15;
    letter-spacing: 1px;
    text-transform: uppercase;
  }
  .brand-mark {
    width: 14px; height: 14px;
    border-radius: 50%;
    background: var(--gold);
    margin: 0 auto 14px;
  }
  .trade-label {
    margin-top: 18px;
    color: var(--gold);
    font-size: 15px;
    letter-spacing: 7px;
  }
  .divider {
    position: absolute;
    left: 312px; top: 80px;
    width: 2px; height: 200px;
    background: var(--gold);
  }
  .contact-block {
    position: absolute;
    left: 340px; top: 82px;
  }
  .person-name {
    font-family: "Playfair Display", serif;
    font-weight: 700;
    color: var(--gold);
    font-size: 34px;
    letter-spacing: 1px;
    text-transform: uppercase;
    margin-bottom: 18px;
  }
  .contact-list { list-style: none; }
  .contact-item {
    display: flex;
    align-items: center;
    gap: 10px;
    color: var(--silver);
    font-size: 19px;
    line-height: 36px;
  }
  .contact-item svg { width: 18px; height: 18px; flex: none; }
  .credentials {
    position: absolute;
    left: 0; right: 0; bottom: 48px;
    text-align: center;
    color: var(--silver);
    font-size: 22px;
    line-height: 1.35;
  }

  /* Back */
  .back-brand {
    position: absolute;
    right: 60px; top: 110px;
    width: 260px;
    text-align: center;
  }
  .back-brand .brand-name { font-size: 34px; }
  .services {
    position: absolute;
    left: 40px; top: 300px;
    color: var(--silver);
    font-size: 17px;
    line-height: 30px;
    list-style: none;
  }
  .services-row { display: flex; gap: 14px; flex-wrap: wrap; }
  .service::before {
    content: "";
    display: inline-block;
    width: 7px; height: 7px;
    border-radius: 50%;
    background: var(--gold);
    margin-right: 7px;
    vertical-align: middle;
  }
</style>
</head>
<body>

<section class="card card-front">
  <div class="brand-block">
    <div class="brand-mark"></div>
    <div class="brand-name">Brackenfold Latches</div>
    <div class="trade-label">LOCKSMITH</div>
  </div>
  <div class="divider"></div>
  <div class="contact-block">
    <h1 class="person-name">Rob Fenwick</h1>
    <ul class="contact-list">
      <li class="contact-item">
        <svg viewBox="0 0 18 18"><rect x="4" y="1" width="10" height="16" rx="2" fill="none" stroke="#d9a821" stroke-width="2"/><circle cx="9" cy="14" r="1" fill="#d9a821"/></svg>
        07841592637
      </li>
      <li class="contact-item">
        <svg viewBox="0 0 18 18"><path d="M2 6c0-3 14-3 14 0v2h-4V6H6v2H2z" fill="#d9a821"/><rect x="3" y="9" width="12" height="7" rx="1" fill="#d9a821"/></svg>
        01823 574419
      </li>
      <li class="contact-item">
        <svg viewBox="0 0 18 18"><rect x="1" y="3" width="16" height="12" fill="#d9a821"/><path d="M1 3l8 7 8-7" fill="none" stroke="#151516" stroke-width="1.5"/></svg>
        contact@brackenfoldlatches.com
      </li>
      <li class="contact-item">
        <svg viewBox="0 0 18 18"><circle cx="9" cy="9" r="8" fill="#d9a821"/><path d="M1 9h16M9 1c-4 4-4 12 0 16M9 1c4 4 4 12 0 16" fill="none" stroke="#151516" stroke-width="1"/></svg>
        www.brackenfoldlatches.com
      </li>
    </ul>
  </div>
  <p class="credentials">Accredited Guild &amp; Tower KSR Level 3, QTRB<br>Fully Insured &amp; PVX Checked</p>
</section>

<section class="card card-back">
  <div class="back-brand">
    <div class="brand-mark"></div>
    <div class="brand-name">Brackenfold Latches</div>
  </div>
  <ul class="services">
    <li class="services-row">
      <span class="service">Emergency Lock Out</span>
      <span class="service">New Lock Fitting &amp; Replacement</span>
      <span class="service">High Security Upgrades</span>
    </li>
    <li class="services-row">
      <span class="service">UPVC lock repairs</span>
      <span class="service">Free Security Reviews</span>
      <span class="service">Mobile Key Cutting</span>
    </li>
  </ul>
</section>

</body>
</html>
```